Brin’s Beauty. Coffee Scrub Skincare

Graphic design for my Coffee Scrub skin care business. Brin’s Beauty. To go on the packaging. Fun with pastel colours, but still clean and professional. See attached photos on similar businesses packaging. I like the “Tala & Wren” font (see attached photo).

Things to write on the packaging: Brin’s Beauty. Recycled Coffee scrub. Coconut and Chocolate. Recycled packaging. Vegan. Not tested on animal. Recycled coffee. Pink Australian clay. 150g 5.29 oz. Made in Australia.

```html
<!DOCTYPE html>
<html lang="en">
<head>
<meta charset="utf-8">
<title>Brin’s Beauty – Recycled Coffee Scrub labels</title>
<link href="https://fonts.googleapis.com/css2?family=Montserrat:wght@800&family=Poppins:wght@400;500;600&display=swap" rel="stylesheet">
<style>
  :root{
    --teal:#90cdcc;
    --navy:#0b2a40;
    --ink:#0f2b3d;
    --white:#ffffff;
    --frame:#1a1a1a;
  }
  *{box-sizing:border-box;margin:0;padding:0}
  html,body{width:1200px;height:1200px;overflow:hidden;background:var(--white)}
  body{font-family:"Poppins",sans-serif;color:var(--ink);position:relative}

  .label-row{position:absolute;left:24px;top:363px;display:flex;gap:18px}
  .label{width:372px;height:474px;position:relative}

  /* shared type */
  .kicker{font-family:"Poppins",sans-serif;font-weight:500;letter-spacing:.22em;font-size:17px;text-align:center}
  .title{font-family:"Montserrat",sans-serif;font-weight:800;font-size:38px;letter-spacing:-.01em;text-align:center;line-height:1}
  .rule{height:3px;width:170px;margin:7px auto 6px}
  .flavour{font-size:13.5px;text-align:center}
  .brand{font-family:"Poppins",sans-serif;font-weight:600;color:var(--white);text-align:center;line-height:1}
  .tagline{font-size:4.5px;letter-spacing:.2em;text-align:center;color:var(--white);margin-top:3px;text-transform:uppercase}
  .pattern{background:var(--navy)}
  svg.wave{display:block;width:100%}

  /* label 1: white front */
  .front{border:1.5px solid var(--frame)}
  .front-inner{position:absolute;inset:9px;border:1.5px solid var(--navy);overflow:hidden;background:var(--white)}
  .front-pattern{position:absolute;left:0;top:0;right:0;height:216px}
  .front-brandbox{position:absolute;left:107px;top:0;width:128px}
  .front-brandbox .box{background:var(--teal);height:102px;display:flex;flex-direction:column;justify-content:center;align-items:center}
  .front-brandbox .brand{font-size:17px}
  .front-band{position:absolute;left:0;right:0;top:200px;height:7px;background:var(--teal)}
  .front-copy{position:absolute;left:0;right:0;top:252px}
  .front-copy .kicker{color:var(--ink)}
  .front-copy .title{color:var(--teal);margin-top:4px}
  .front-copy .rule{background:var(--navy)}
  .front-copy .flavour{color:var(--ink)}
  .claims{font-size:8.4px;text-align:center;line-height:1.35;margin:26px auto 0;width:250px;color:#111}
  .origin{font-size:10px;text-align:center;line-height:1.3;margin-top:22px;color:var(--ink)}

  /* label 2: teal back */
  .back{border:1.5px solid var(--frame)}
  .back-inner{position:absolute;inset:10px 10px 10px 10px;background:var(--teal);overflow:hidden;border:1.5px solid var(--navy)}
  .back-brand{margin-top:18px}
  .back-brand .brand{font-size:17px}
  .back-copy{margin-top:36px}
  .back-copy .kicker{color:var(--white)}
  .back-copy .title{color:var(--white);margin-top:4px}
  .back-copy .rule{background:var(--white);height:1.5px}
  .back-copy .flavour{color:var(--white)}
  .badges{width:90px;margin:9px auto 0;border:1px solid var(--white);text-align:center;color:var(--white)}
  .badges .small{font-size:5.5px;padding:2px 0;border-bottom:1px solid var(--white)}
  .badges .big{font-size:8.5px;padding:2px 0}
  .back-origin{font-size:10px;text-align:center;line-height:1.3;margin-top:26px;color:var(--ink)}
  .back-pattern{position:absolute;left:0;right:0;bottom:0;height:160px}
  .back-pattern .pattern{height:144px}

  /* label 3: brand sheet */
  .sheet-top{height:338px;position:relative}
  .sheet-top .fill{background:var(--teal);height:322px;display:flex;flex-direction:column;align-items:center;justify-content:center;padding-top:20px}
  .sheet-top .brand{font-size:50px;letter-spacing:-.01em}
  .sheet-top .tagline{font-size:12px;letter-spacing:.22em;margin-top:10px}
  .sheet-copy{margin-top:14px}
  .sheet-copy .kicker{color:var(--ink)}
  .sheet-copy .title{color:var(--teal);margin-top:4px}
  .sheet-copy .rule{background:var(--navy)}
  .sheet-copy .flavour{color:var(--ink)}
</style>
</head>
<body>
<main class="label-row">

  <!-- Front label -->
  <section class="label front">
    <div class="front-inner">
      <div class="front-pattern pattern" role="img" aria-label="Navy background scattered with pastel squiggles, zigzags and small triangles"></div>
      <div class="front-band"></div>
      <div class="front-brandbox">
        <div class="box">
          <p class="brand">BRIN’S BEAUTY</p>
          <p class="tagline">Natural Skincare</p>
        </div>
        <svg class="wave" viewBox="0 0 100 8" preserveAspectRatio="none" height="8" aria-hidden="true">
          <path fill="var(--teal)" d="M0 0H100V4Q95 8 90 4T80 4T70 4T60 4T50 4T40 4T30 4T20 4T10 4T0 4Z"/>
        </svg>
      </div>
      <div class="front-copy">
        <p class="kicker">RECYCLED</p>
        <h1 class="title">COFFEE SCRUB</h1>
        <div class="rule"></div>
        <p class="flavour">Coconut and Chocolate</p>
        <p class="claims">Recycled packaging. Vegan. Not tested on animal. Recycled coffee. Pink Australian clay.</p>
        <p class="origin">Made in Australia.<br>150g 5.29 oz</p>
      </div>
    </div>
  </section>

  <!-- Back label -->
  <section class="label back">
    <div class="back-inner">
      <div class="back-brand">
        <p class="brand">BRIN’S BEAUTY</p>
        <p class="tagline">Natural Skincare</p>
      </div>
      <div class="back-copy">
        <p class="kicker">RECYCLED</p>
        <h2 class="title">COFFEE SCRUB</h2>
        <div class="rule"></div>
        <p class="flavour">Coconut and Chocolate</p>
        <div class="badges">
          <p class="small">Vegan, Not tested on animal</p>
          <p class="big">Recycled coffee</p>
        </div>
        <p class="back-origin">Made in Australia.<br>150g 5.29 oz</p>
      </div>
      <div class="back-pattern">
        <svg class="wave" viewBox="0 0 100 8" preserveAspectRatio="none" height="16" aria-hidden="true">
          <path fill="var(--navy)" d="M0 4Q5 0 10 4T20 4T30 4T40 4T50 4T60 4T70 4T80 4T90 4T100 4V8H0Z"/>
        </svg>
        <div class="pattern" role="img" aria-label="Navy background scattered with pastel squiggles, zigzags and small triangles"></div>
      </div>
    </div>
  </section>

  <!-- Brand sheet -->
  <section class="label sheet">
    <div class="sheet-top">
      <div class="fill">
        <p class="brand">BRIN’S BEAUTY</p>
        <p class="tagline">Natural Skincare</p>
      </div>
      <svg class="wave" viewBox="0 0 100 8" preserveAspectRatio="none" height="16" aria-hidden="true">
        <path fill="var(--teal)" d="M0 0H100V4Q95 8 90 4T80 4T70 4T60 4T50 4T40 4T30 4T20 4T10 4T0 4Z"/>
      </svg>
    </div>
    <div class="sheet-copy">
      <p class="kicker">RECYCLED</p>
      <h2 class="title">COFFEE SCRUB</h2>
      <div class="rule"></div>
      <p class="flavour">Coconut and Chocolate</p>
    </div>
  </section>

</main>
</body>
</html>
```